Card design for orthopaedic surgeons working as The Brindlewood Orthopaedic Centre

Business cards, letterhead

Colors

Designer to choose colors to be used in the design.

Requirements
Must have
• Late addition.
• Cards letterhead must have logos of
• Corvane Federated Institute of Surgeons
• Meridale Orthopaedic Society
Nice to have
• Back of card to have space for appointment time to be added by hand and some blank space for writing incidental other notes.

```html
<!DOCTYPE html>
<html lang="en">
<head>
<meta charset="utf-8">
<title>The Brindlewood Orthopaedic Centre – Business Card</title>
<link href="https://fonts.googleapis.com/css2?family=Lato:wght@400;700&family=Montserrat:wght@400&family=Arimo:wght@700&display=swap" rel="stylesheet">
<style>
  :root{
    --navy:#0b3350;
    --navy-deep:#0c2c47;
    --sky:#36a8ee;
    --white:#ffffff;
    --backdrop:#e9ecef;
    --badge:#d5dde4;
  }
  html,body{margin:0;padding:0;overflow:hidden;}
  body{width:1200px;height:900px;background:var(--backdrop);position:relative;font-family:"Lato",sans-serif;}
  .card{position:absolute;width:555px;height:343px;overflow:hidden;box-shadow:0 3px 8px rgba(0,0,0,.25);}
  .card--front{left:330px;top:90px;background:var(--white);}
  .card--back{left:332px;top:470px;background:var(--navy);}

  .card__wave-band{position:absolute;left:0;top:150px;width:555px;height:90px;
    background:linear-gradient(170deg,var(--white) 0%,var(--white) 30%,var(--sky) 55%,var(--navy-deep) 100%);}
  .card__lower{position:absolute;left:0;top:240px;width:555px;height:103px;background:var(--navy);}
  .card__lower--tall{top:200px;height:143px;}

  .brand-name{position:absolute;margin:0;font-family:"Montserrat",sans-serif;font-weight:400;font-size:17px;letter-spacing:-.5px;color:var(--sky);white-space:nowrap;}
  .card--front .brand-name{left:25px;top:90px;}
  .card--back .brand-name{left:0;right:0;top:173px;text-align:center;font-size:18px;}

  .member-badges{position:absolute;right:26px;top:22px;display:flex;gap:10px;}
  .member-badge{width:34px;height:34px;border-radius:50%;background:var(--badge);}

  .holder{position:absolute;left:23px;top:276px;color:var(--white);}
  .holder__name{margin:0;font-family:"Arimo",sans-serif;font-weight:700;font-size:20px;letter-spacing:.3px;line-height:1.1;}
  .holder__role{margin:2px 0 0 1px;font-size:15.5px;line-height:1.2;}

  .contact{position:absolute;right:27px;top:213px;margin:0;padding:0;list-style:none;color:var(--white);font-size:15.5px;text-align:right;}
  .contact__line{display:flex;justify-content:flex-end;align-items:center;gap:3px;height:20.5px;}
  .contact__line svg{width:13px;height:13px;fill:var(--white);}
  .contact__address{margin-top:7px;line-height:20px;}
</style>
</head>
<body>
  <section class="card card--front">
    <div class="card__wave-band" role="img" aria-label="Flowing navy and sky-blue wave band"></div>
    <div class="card__lower card__lower--tall"></div>
    <div class="member-badges">
      <span class="member-badge" role="img" aria-label="Corvane Federated Institute of Surgeons membership badge"></span>
      <span class="member-badge" role="img" aria-label="Meridale Orthopaedic Society membership badge"></span>
    </div>
    <p class="brand-name">The Brindlewood Orthopaedic Centre</p>
    <ul class="contact">
      <li class="contact__line">055-284 613 902<svg viewBox="0 0 16 16"><path d="M2 6c0-2 2.5-3 6-3s6 1 6 3v1.5h-3V6H5v1.5H2z M4 8.5h8l1.5 5h-11z"/></svg></li>
      <li class="contact__line">info@brindlewd.com<svg viewBox="0 0 16 16"><path d="M1 3h14v10H1z M2 4.5v.5l6 4 6-4v-.5z" fill-rule="evenodd"/></svg></li>
      <li class="contact__line">www.brindlewood.com<svg viewBox="0 0 16 16"><circle cx="8" cy="8" r="7"/></svg></li>
      <li class="contact__address">17, Harrow Lane<br>Kestonby, 60218,Avelmark</li>
    </ul>
    <div class="holder">
      <p class="holder__name">CALLUM ARDLEY</p>
      <p class="holder__role">Managing Director</p>
    </div>
  </section>

  <section class="card card--back">
    <p class="brand-name">The Brindlewood Orthopaedic Centre</p>
  </section>
</body>
</html>
```